Postcard Design

We are Professional, quick and efficient. We are State Licensed and Insured. Gas•Water•Sewer Specializing in all of the customers plumbing needs. We accept credit cards. The law in Louisiana is that I have company address, and license number on all advertising. License number is LMP 4129. Address is 20917 north cedar rd. Marsh Point, Ms. 70512

```html
<!DOCTYPE html>
<html lang="en">
<head>
<meta charset="utf-8">
<title>Plumbing Postcard</title>
<link rel="stylesheet" href="https://fonts.googleapis.com/css2?family=Roboto+Condensed:ital,wght@0,400;0,700;0,800;1,700;1,800&display=swap">
<style>
  :root {
    --page-bg: #ecebe8;
    --brand-red: #e3222b;
    --brand-red-dark: #b8141c;
    --ink: #111111;
    --white: #ffffff;
    --photo-light: #e9eaec;
    --photo-mid: #b9bcc1;
    --photo-dark: #5b5f66;
    --muted: #333333;
  }
  * { box-sizing: border-box; margin: 0; padding: 0; }
  html, body {
    width: 1200px; height: 1000px; overflow: hidden;
    background: var(--page-bg);
    font-family: "Roboto Condensed", "Arial Narrow", sans-serif;
  }
  .postcard {
    position: absolute; left: 220px; width: 760px; height: 450px;
    overflow: hidden; background: var(--white);
    box-shadow: 0 6px 18px rgba(0,0,0,.18);
  }
  .postcard--front { top: 28px; }
  .postcard--back { top: 518px; }

  .photo { position: absolute; inset: 0; }
  .postcard--front .photo {
    background: linear-gradient(100deg, var(--photo-dark) 0%, var(--photo-mid) 30%, var(--photo-light) 60%, #f4f4f5 100%);
  }
  .postcard--back .photo {
    background: linear-gradient(110deg, var(--photo-mid) 0%, var(--photo-light) 35%, var(--photo-mid) 60%, var(--photo-light) 100%);
  }
  .layer { position: absolute; inset: 0; }

  /* Front */
  .tab-text {
    position: absolute; left: 450px; width: 310px; top: 34px;
    text-align: center; color: var(--white);
  }
  .tab-headline {
    font-weight: 800; font-style: italic; font-size: 31px; line-height: 1.12;
    text-transform: uppercase;
  }
  .tab-license { font-weight: 700; font-size: 17px; margin-top: 10px; }
  .tab-services { font-weight: 700; font-size: 29px; margin-top: 10px; }
  .front-tagline {
    position: absolute; right: 44px; top: 306px; width: 210px;
    text-align: center; font-weight: 800; font-style: italic;
    font-size: 27px; line-height: 1.15; color: var(--ink);
  }
  .front-phone {
    position: absolute; left: 24px; top: 380px;
    font-weight: 800; font-size: 54px; line-height: 1; color: var(--brand-red);
    letter-spacing: -0.5px;
  }
  .front-cards {
    position: absolute; right: 30px; bottom: 14px;
    font-size: 14px; color: var(--muted);
  }

  /* Back */
  .back-services {
    position: absolute; left: 24px; top: 20px;
    font-weight: 800; font-size: 30px; color: var(--brand-red);
    text-shadow: 0 0 3px var(--white), 0 0 3px var(--white);
  }
  .back-tagline {
    position: absolute; left: 24px; top: 62px; width: 340px;
    font-weight: 800; font-style: italic; font-size: 31px; line-height: 1.08;
    color: var(--ink);
    text-shadow: 0 0 3px var(--white), 0 0 3px var(--white);
  }
  .back-phone {
    position: absolute; left: 22px; top: 140px;
    font-weight: 800; font-size: 52px; color: var(--brand-red);
    text-shadow: 0 0 4px var(--white), 0 0 4px var(--white), 0 0 4px var(--white);
  }
  .company-details {
    position: absolute; left: 410px; top: 22px;
    font-weight: 700; font-size: 17px; line-height: 1.3; color: var(--ink);
  }
  .company-details .license-note { margin-top: 16px; }
  .stamp-box {
    position: absolute; right: 24px; top: 24px; width: 96px; height: 118px;
    background: rgba(255,255,255,.55);
  }
  .mailing-area {
    position: absolute; right: 24px; top: 210px; width: 300px; height: 220px;
    background: rgba(255,255,255,.82);
  }
  .indicia-strip {
    position: absolute; left: 330px; bottom: 20px; width: 110px; height: 60px;
    background: rgba(255,255,255,.7);
  }
</style>
</head>
<body>

<section class="postcard postcard--front">
  <div class="photo" role="img" aria-label="Photo of a smiling plumber under a sink holding an orange-handled adjustable wrench beside black drain pipes"></div>
  <svg class="layer" width="760" height="450" viewBox="0 0 760 450" aria-hidden="true">
    <defs>
      <linearGradient id="tabRed" x1="0" y1="0" x2="1" y2="1">
        <stop offset="0" stop-color="#ef2d35"/>
        <stop offset="1" stop-color="#c5161e"/>
      </linearGradient>
    </defs>
    <path d="M0,450 L0,420 Q300,350 560,330 Q680,322 760,340 L760,450 Z" fill="rgba(255,255,255,.35)"/>
    <path d="M468,0 H760 V240 L478,196 Q448,190 448,162 V22 Q448,0 468,0 Z" fill="url(#tabRed)"/>
    <path d="M448,162 Q448,190 478,196 L760,240" fill="none" stroke="var(--brand-red-dark)" stroke-width="3"/>
  </svg>
  <div class="tab-text">
    <p class="tab-headline">Professional,<br>Quick &amp; Efficient</p>
    <p class="tab-license">State Licensed &amp; Insured.</p>
    <p class="tab-services">Gas • Water • Sewer</p>
  </div>
  <p class="front-tagline">Specializing in<br>all your plumbing<br>needs.</p>
  <p class="front-phone">123-456-7890</p>
  <p class="front-cards">We accept credit cards.</p>
</section>

<section class="postcard postcard--back">
  <div class="photo" role="img" aria-label="Faded photo of the plumber at a kitchen sink with drain pipes and a wrench"></div>
  <div class="stamp-box"></div>
  <div class="mailing-area"></div>
  <div class="indicia-strip"></div>
  <p class="back-services">GAS • WATER • SEWER</p>
  <p class="back-tagline">Specializing in all your plumbing needs.</p>
  <p class="back-phone">123-456-7890</p>
  <div class="company-details">
    <p>LMP 4129</p>
    <p>20917 north cedar rd.</p>
    <p>Marsh Point, Ms. 70512</p>
    <p class="license-note">STATE LICENSED &amp; INSURED.</p>
  </div>
</section>

</body>
</html>
```